依頼詳細
◇サイトマップ
①Home
②MENU&PRICE
③SALON INFO
④PRODUCTS
⑤COUPON
⑥GALLERY
⑦STAFF
⑧VOICE
⑨RECRUIT
⑩CONTACT
⑪BLOG(一覧)
⑫NEWS(一覧)
⑬CAT
⑭HAIR CARE

◇優先事項
1.ユーザビリティー
2.凝ったデザイン
3.編集更新

◇期待する効果
1.新規顧客の獲得
2.既存顧客の満足度向上
3.イメージアップ

◇ターゲット
【性別】男女比(男1 : 9女)
【年代】30代~40代
【属性】会社員 自営業 主婦

◇sns
Facebook 会社用

◇テイスト
◯シンプル ナチュラル かっこいい
×可愛い・キュート カラフル 高級感

※デザインのテイストとして僕自身の好みですが、ペンキの質感やコンクリートの質感が好きで、シンプルの中にかっこよさがあるデザインが好きです。
(少しでも参考にして頂ければ嬉しいです)

◇希望カラー
ベース色(ベージュ・白)
差し色 (茶系・緑系 アースカラー)
サイトURL
http://mizutama2047.com/
ページ数
1ページ
希望イメージ
シンプル 複雑
単色 カラフル
暗い 明るい
日常 高級
遊び心 厳粛
未来的 伝統的
女性的 男性的
希望する色
茶系、緑系、グレー系、ペースは白系で考えています。そのほかは茶色や緑が好きです。
納品ファイル
• イラストレーター形式 (.ai)
• フォトショップ形式 (.psd)
• PNG形式 (.png)
補足説明
素材①
撮影データをナギボックスドライブにアップしています。
下記URLよりダウンロードしてください。
http://nagibox.jp/download/c51e7a02d9b3f684e10a7c2bd5f93e8a61c04d77
ダウンロードパスワード pass

※素材として、コンクリートの写真があり、店内の打ちっぱなしの部分になりますが、上手く背景などで使えたらと思い写真を取りました、使えなさそうであれば無視して頂いても構いません。

素材➁
クレパド:https://jp.krepado.com/
当院で定期契約をしています。クレジット購入のみのもの以外をご利用下さい。
また定期契約のものは当院の負担となり、ランサー様に負担はありません。
カンプ画像を入れてください。
依頼公開後の追記内容
素材のダウンロードリンクが切れてしまっていたので再度アップロード致します。
ダウンロードをお願い致します。
http://nagibox.jp/download/9e4c1b7a35d0f28e6a17c9b4e02d5f3a8b76c1e9

ダウンロードパスワード pass

作成期間が少なくなってしまった人もいるので延長させていただきます。
もう少し提案が見たいため、延長させて頂きます。
■ 選んだ理由

デザインが良かったので選定致しました。

■ 提案者全員のお礼・コメント

皆様素敵なデザインをありがとうございました。

```html
<!DOCTYPE html>
<html lang="ja">
<head>
<meta charset="utf-8">
<title>風車 | Hair Salon</title>
<link href="https://fonts.googleapis.com/css2?family=Josefin+Sans:wght@300;400;600&family=Noto+Sans+JP:wght@300;400;500&display=swap" rel="stylesheet">
<style>
:root{
  --ink:#2f2f2f;
  --ink-soft:#6b6b6b;
  --line:#8a8580;
  --paper:#ffffff;
  --beige:#efeae4;
  --stone:#e3e5e7;
  --footer:#4b4a49;
  --footer-ink:#e9e7e4;
  --head:'Josefin Sans',sans-serif;
  --body:'Noto Sans JP',sans-serif;
}
*{box-sizing:border-box;margin:0;padding:0}
html,body{width:1200px;height:3180px;overflow:hidden}
body{background:var(--paper);color:var(--ink);font-family:var(--body);position:relative}

.site-header{position:absolute;top:0;left:0;width:1200px;height:112px}
.menu-toggle{position:absolute;left:36px;top:30px;width:44px;text-align:center}
.menu-toggle span{display:block;height:3px;background:var(--ink);margin-bottom:8px}
.menu-toggle small{font-family:var(--head);font-size:13px;letter-spacing:1px}
.brand{position:absolute;left:0;right:0;top:32px;text-align:center;font-family:var(--body);font-weight:500;font-size:40px;letter-spacing:10px;line-height:48px;color:var(--ink)}
.reserve{position:absolute;right:40px;top:38px;width:150px;height:36px;border:2px solid var(--ink);font-family:var(--head);font-size:16px;letter-spacing:2px;display:flex;align-items:center;justify-content:center}

.hero{position:absolute;top:112px;left:0;width:1200px;height:576px}
.hero .photo{position:absolute}
.p-left{left:0;top:0;width:384px;height:576px;background:linear-gradient(160deg,#c9b8a5,#9c4a3a 45%,#c8a66c 75%,#8c7a69)}
.p-mid-top{left:390px;top:0;width:426px;height:286px;background:linear-gradient(135deg,#6e6a65,#9b948c 60%,#5d5955)}
.p-mid-bot{left:390px;top:294px;width:426px;height:282px;background:linear-gradient(120deg,#d9d6d1,#b8a993 50%,#8d7a64)}
.p-right{left:828px;top:0;width:372px;height:576px;background:linear-gradient(180deg,#f4f1ee,#e6ddd3 55%,#c9b6a1)}
.menu-badge{position:absolute;left:420px;top:22px;width:366px;height:242px;border:3px solid rgba(255,255,255,.9);display:flex;align-items:center;justify-content:center;font-family:var(--head);font-size:30px;letter-spacing:6px;color:#fff}

.section-title{font-family:var(--head);font-weight:400;font-size:30px;letter-spacing:5px;line-height:36px;text-align:center;position:absolute;left:0;width:1200px}

.col-title{position:absolute;width:300px;text-align:center;font-family:var(--head);font-weight:600;font-size:20px;letter-spacing:3px}
.feed{position:absolute;width:400px;list-style:none}
.feed li{display:flex;gap:16px;font-size:13px;line-height:20px;height:56px;color:var(--ink)}
.feed time{flex:0 0 70px;color:var(--ink-soft)}

.menu-band{position:absolute;top:1140px;left:0;width:1200px;height:640px;background:var(--beige);clip-path:polygon(0 40px,1200px 0,1200px 600px,0 640px)}
.price-list{position:absolute;left:224px;top:1320px;width:620px;list-style:none}
.price-list li{display:flex;align-items:center;height:33px;font-size:13px}
.price-list .dots{flex:1;border-bottom:1px solid var(--line);margin:0 16px}
.price-list .price{width:70px;text-align:right}
.more{position:absolute;left:524px;top:1628px;width:152px;height:32px;border:2px solid var(--ink);font-family:var(--head);font-size:14px;letter-spacing:2px;display:flex;align-items:center;justify-content:center}

.faq-list{position:absolute;left:264px;top:1860px;width:700px}
.faq-list dt{font-size:14px;font-weight:500;margin-top:26px;line-height:20px}
.faq-list dt:first-child{margin-top:0}
.faq-list dd{font-size:12px;color:var(--ink-soft);margin-top:6px;line-height:18px}

.access-band{position:absolute;top:2260px;left:0;width:1200px;height:620px;background:var(--stone);clip-path:polygon(0 0,1200px 40px,1200px 620px,0 620px)}
.map{position:absolute;left:60px;top:2456px;width:412px;height:376px;background:linear-gradient(135deg,#efece4,#dde3d6 50%,#e9e2d2)}
.address{position:absolute;left:504px;top:2460px;font-size:13px;line-height:22px}
.address p+p{margin-top:16px}
.pin{position:absolute;left:255px;top:2620px}

.site-footer{position:absolute;top:2880px;left:0;width:1200px;height:300px;background:var(--footer);color:var(--footer-ink)}
.site-footer .brand{top:44px;color:var(--footer-ink)}
.footer-nav{position:absolute;left:312px;top:110px;display:flex;gap:44px;list-style:none}
.footer-nav > li{font-family:var(--head);font-size:17px;letter-spacing:1px}
.footer-nav ul{list-style:none;margin-top:8px}
.footer-nav ul li{font-size:13px;line-height:20px;font-family:var(--head)}
.copyright{position:absolute;bottom:16px;width:1200px;text-align:center;font-family:var(--head);font-size:12px;letter-spacing:1px}
</style>
</head>
<body>

<header class="site-header">
  <div class="menu-toggle"><span></span><span></span><span></span><small>MENU</small></div>
  <div class="brand">風車</div>
  <div class="reserve">Reserve</div>
</header>

<section class="hero">
  <div class="photo p-left" role="img" aria-label="店内の装飾オブジェの写真"></div>
  <div class="photo p-mid-top" role="img" aria-label="サロン入口の看板の写真"></div>
  <div class="menu-badge">MENU</div>
  <div class="photo p-mid-bot" role="img" aria-label="ヘアカット用のハサミの写真"></div>
  <div class="photo p-right" role="img" aria-label="ヘアスタイルのモデル写真"></div>
</section>

<section class="information">
  <h2 class="section-title" style="top:776px">Information</h2>
  <h3 class="col-title" style="left:180px;top:838px">News</h3>
  <ul class="feed" style="left:164px;top:884px">
    <li><time>2017.07.28</time><span>ニュースが入ります。ニュースが入ります。ニュースが入ります。</span></li>
    <li><time>2017.07.28</time><span>ニュースが入ります。ニュースが入ります。</span></li>
    <li><time>2017.07.28</time><span>ニュースが入ります。ニュースが入ります。</span></li>
    <li><time>2017.07.28</time><span>ニュースが入ります。ニュースが入ります。ニュースが入ります。</span></li>
  </ul>
  <h3 class="col-title" style="left:730px;top:838px">Blog</h3>
  <ul class="feed" style="left:664px;top:884px">
    <li><time>2017.07.28</time><span>ブログが入ります。ブログが入ります。ブログが入ります。</span></li>
    <li><time>2017.07.28</time><span>ブログが入ります。ブログが入ります。</span></li>
    <li><time>2017.07.28</time><span>ブログが入ります。ブログが入ります。</span></li>
    <li><time>2017.07.28</time><span>ブログが入ります。ブログが入ります。ブログが入ります。</span></li>
  </ul>
</section>

<div class="menu-band"></div>
<section class="menu">
  <h2 class="section-title" style="top:1244px">Menu</h2>
  <ul class="price-list">
    <li><span>シャンプー・カット</span><span class="dots"></span><span class="price">¥4,000</span></li>
    <li><span>前カット</span><span class="dots"></span><span class="price">¥500</span></li>
    <li><span>カラー</span><span class="dots"></span><span class="price">¥4,500~</span></li>
    <li><span>ブリーチ</span><span class="dots"></span><span class="price">¥7,000~</span></li>
    <li><span>パーマ</span><span class="dots"></span><span class="price">¥5,000~</span></li>
    <li><span>縮毛矯正（ストレート）</span><span class="dots"></span><span class="price">¥15,000~</span></li>
    <li><span>トリートメント</span><span class="dots"></span><span class="price">¥3,000~</span></li>
    <li><span>ヘアエステ</span><span class="dots"></span><span class="price">¥3,000~</span></li>
  </ul>
  <div class="more">And More</div>
</section>

<section class="faq">
  <h2 class="section-title" style="top:1806px">FAQ</h2>
  <dl class="faq-list">
    <dt>何時から開いていますか？</dt><dd>10時から営業しております。</dd>
    <dt>ネット予約はしていますか？</dt><dd>ホームページからご予約いただけます。</dd>
    <dt>駐車場は近くにありますか？</dt><dd>提携駐車場をご利用ください。近くにコインパーキングもございます。</dd>
    <dt>クレジットカードは使えますか？</dt><dd>各種カードをご利用いただけます。</dd>
    <dt>子供のカットもしてもらえますか？</dt><dd>もちろんできます。</dd>
  </dl>
</section>

<div class="access-band"></div>
<section class="access">
  <h2 class="section-title" style="top:2384px">Access</h2>
  <div class="map" role="img" aria-label="サロン周辺の地図"></div>
  <svg class="pin" width="22" height="30" viewBox="0 0 22 30" aria-hidden="true"><path d="M11 0C5 0 0 5 0 11c0 8 11 19 11 19s11-11 11-19C22 5 17 0 11 0z" fill="#c0392b"/><circle cx="11" cy="11" r="4" fill="#fff"/></svg>
  <div class="address">
    <p>〒000-0000<br>港南県緑川市本町二丁目7-3</p>
    <p>緑川駅から徒歩5分<br>本町バス停から徒歩2分</p>
    <p>TEL:000-111-2222</p>
    <p>営業時間<br>平日 10:00～19:00（最終受付18:00）<br>土日祝 9:00～18:00<br>定休日：毎週火曜日</p>
  </div>
</section>

<footer class="site-footer">
  <div class="brand">風車</div>
  <ul class="footer-nav">
    <li>Home</li>
    <li>Salon<ul><li>Salon Info</li><li>Menu</li><li>Staff</li><li>Recruit</li><li>Coupon</li></ul></li>
    <li>Menu<ul><li>Price</li><li>Cat</li><li>Hair Care</li></ul></li>
    <li>Gallery<ul><li>Hair Catalogue</li><li>Products</li></ul></li>
    <li>Blog</li>
    <li>Contact</li>
  </ul>
  <p class="copyright">Copyright All Rights Reserved</p>
</footer>

</body>
</html>
```